BrovaLT BIZ Card, email signature & Stationary

Professional business cards, email signatures and ms word letterhead

Target Market(s)

business owners

Industry/Entity Type

cloud hosting

Contact Information for Business Card

name title office phone number , direct line, fax email address web site

Font styles to use
Other font styles liked:
• something that compliments font in logo

```html
<!DOCTYPE html>
<html lang="en">
<head>
<meta charset="utf-8">
<title>BrovaLT Business Cards</title>
<link rel="stylesheet" href="https://fonts.googleapis.com/css2?family=Montserrat:ital,wght@0,300;0,400;0,600;1,700&family=Open+Sans:ital,wght@0,400;0,600;1,400&display=swap">
<style>
  :root {
    --brand-red: #ed1c24;
    --ink: #111111;
    --card-black: #000000;
    --card-white: #ffffff;
    --page: #ffffff;
    --card-shadow: rgba(0, 0, 0, 0.45);
  }
  * { margin: 0; padding: 0; box-sizing: border-box; }
  html, body {
    width: 1054px;
    height: 1200px;
    overflow: hidden;
    background: var(--page);
  }
  .sheet {
    position: relative;
    width: 1054px;
    height: 1200px;
  }
  .card {
    position: absolute;
    width: 546px;
    height: 311px;
    box-shadow: 5px 5px 6px var(--card-shadow);
    overflow: hidden;
  }
  .card--front-dark { left: 233px; top: 126px; background: var(--card-black); }
  .card--back { left: 238px; top: 471px; background: var(--card-white); }
  .card--front-light { left: 237px; top: 829px; background: var(--card-white); }

  /* Left brand panel, where the brand's decorative mark sits */
  .brand-panel {
    position: absolute;
    left: 0;
    top: 0;
    width: 160px;
    height: 100%;
    background: var(--card-black);
  }
  .card--front-dark .brand-panel { background: var(--card-white); }
  .brand-panel__accent {
    position: absolute;
    left: 0;
    bottom: 0;
    width: 100%;
    height: 14px;
    background: var(--brand-red);
  }

  .wordmark {
    position: absolute;
    left: 208px;
    top: 124px;
    font-family: "Montserrat", sans-serif;
    font-weight: 300;
    font-size: 72px;
    line-height: 1;
    letter-spacing: -1px;
    color: var(--brand-red);
  }

  .contact__name {
    position: absolute;
    left: 241px;
    top: 58px;
    font-family: "Montserrat", sans-serif;
    font-weight: 400;
    font-size: 26px;
    letter-spacing: 1px;
    color: var(--ink);
  }
  .contact__title {
    position: absolute;
    left: 304px;
    top: 87px;
    font-family: "Montserrat", sans-serif;
    font-weight: 700;
    font-style: italic;
    font-size: 18px;
    color: var(--brand-red);
  }
  .contact__phone {
    position: absolute;
    left: 258px;
    top: 131px;
    font-family: "Open Sans", sans-serif;
    font-weight: 400;
    font-size: 25px;
    letter-spacing: 0.3px;
    color: var(--ink);
  }
  .contact__row {
    position: absolute;
    left: 250px;
    display: flex;
    align-items: center;
    gap: 16px;
    font-family: "Open Sans", sans-serif;
    font-style: italic;
    font-size: 15.5px;
    color: var(--ink);
  }
  .contact__row--web { top: 194px; }
  .contact__row--mail { top: 244px; }
  .contact__icon { width: 26px; height: 20px; flex: none; }
</style>
</head>
<body>
<main class="sheet">

  <section class="card card--front-dark" aria-label="Business card front, dark">
    <div class="brand-panel" role="img" aria-label="Brand decoration area">
      <div class="brand-panel__accent"></div>
    </div>
    <div class="wordmark">BrovaLT</div>
  </section>

  <section class="card card--back" aria-label="Business card back with contact details">
    <div class="brand-panel" role="img" aria-label="Brand decoration area">
      <div class="brand-panel__accent"></div>
    </div>
    <p class="contact__name">Daniel Marsh</p>
    <p class="contact__title">Manager</p>
    <p class="contact__phone">840 0770 060 70</p>
    <p class="contact__row contact__row--web">
      <svg class="contact__icon" viewBox="0 0 26 20" aria-hidden="true">
        <circle cx="12" cy="10" r="9" fill="var(--brand-red)"/>
        <ellipse cx="12" cy="10" rx="4" ry="9" fill="none" stroke="#fff" stroke-width="1.4"/>
        <line x1="3" y1="10" x2="21" y2="10" stroke="#fff" stroke-width="1.4"/>
      </svg>
      <span>www.yourwebsite.com</span>
    </p>
    <p class="contact__row contact__row--mail">
      <svg class="contact__icon" viewBox="0 0 26 20" aria-hidden="true">
        <rect x="0" y="2" width="26" height="16" fill="var(--brand-red)"/>
        <polyline points="0,2 13,12 26,2" fill="none" stroke="#fff" stroke-width="1.6"/>
        <line x1="0" y1="18" x2="10" y2="10" stroke="#fff" stroke-width="1.2"/>
        <line x1="26" y1="18" x2="16" y2="10" stroke="#fff" stroke-width="1.2"/>
      </svg>
      <span>youremail@mailbox.com</span>
    </p>
  </section>

  <section class="card card--front-light" aria-label="Business card front, light">
    <div class="brand-panel" role="img" aria-label="Brand decoration area">
      <div class="brand-panel__accent"></div>
    </div>
    <div class="wordmark">BrovaLT</div>
  </section>

</main>
</body>
</html>
```